label for selfmade spirits, start-up, quality product

Hey there, my name is Tobias, I am 24 years old, living in the southwest of Germany. In the last two years I did experiment: I produced my own spirits. I used self-produced fruit and distilled it in my families small distillery. Distilling has been a tradition in my family, now I want to start my own production and sales. In our region distilling fruit is a tradition but it is in the hand of well-established families / producers. I am planning to establish a quality product with a modern design to focus more on younger people and to sell my spirits to bars, restaurants and private consumers. I did two varieties: "Jojo plum variety" and "Mirabelle de Nancy". (Mirabelle) I am looking for a label design. The bottles will have 0.7 liters, white glass (due to the clear color of the spirits), in a modern bottle: https://www.glasbergkontor.de/behaelter-und-karaffen/destillate/destillatflaschen/rigel-418 , html taste: clear and noble fruit character in the nose, fine flavor of the respective fruit. During the distillation process I tried to capture the natural aroma of the fruit. Therefore, I did a 2nd distilation which is a special feature, that not everybody does. Jojo Zwetschgen Brand "/" Mirabelle de Nancy Brand "- I am also open for. The design can be: - simple and classy, ​​with a valuable appearance that shows in its font, which is the product itself 3 generations were involved in the production, my grandpa gave me important hints, .. I am so open for all ideas that could catch the target group. the label could be printed on either a white or cream label paper. If you have any questions don`t hesitate to contact me, I am looking forward to your suggestions! Cheers!

Target Market(s)

young adults, urban people, people with an interest in a high quality product, ars / restaurants / private customers

Font styles to use
Decorative
Script

Colors

Designer to choose colors to be used in the design.

Requirements
Must have
• So, there are some things that have been posted on the label, due to legal restrictions: - my address: Tobias Wendelbrunn, Lindenweg 5, 68417 Vogtsburg - alcohol level: "alc. 42% vol." - capacity: "0.70 L"; size at least 4 mm - batch number: "L"; please leave an empty space to fill in by hand this information has not been discussed, but should not be too much in the foreground, nor attract to much attention.

```html
<!DOCTYPE html>
<html lang="de">
<head>
<meta charset="utf-8">
<title>Brand Labels – Mirabelle de Nancy &amp; Jojo Zwetschgen</title>
<link rel="stylesheet" href="https://fonts.googleapis.com/css2?family=Abril+Fatface&family=Josefin+Sans:wght@300;400&family=Poiret+One&display=swap">
<style>
  :root {
    --page: #e9e9ea;
    --label-paper: #f7f0e2;
    --damask: #efe5d3;
    --gold: #d6b566;
    --gold-light: #ead39a;
    --copper: #d8735a;
    --ink: #3a3430;
  }
  * { box-sizing: border-box; margin: 0; padding: 0; }
  html, body {
    width: 1200px; height: 726px; overflow: hidden;
    background: var(--page);
  }
  .sheet {
    width: 1200px; height: 726px;
    display: flex; justify-content: center; align-items: center; gap: 60px;
  }
  .label {
    position: relative;
    width: 520px; height: 480px;
    background: var(--label-paper);
    box-shadow: 0 2px 10px rgba(0,0,0,.12);
    color: var(--ink);
    text-align: center;
  }
  .label__pattern {
    position: absolute; inset: 18px;
    background: radial-gradient(ellipse at center, var(--damask) 0%, #f3ead9 70%, var(--damask) 100%);
  }
  .label__frame {
    position: absolute; inset: 12px;
    border: 3px solid var(--gold);
    outline: 1px solid var(--gold-light);
    outline-offset: -9px;
  }
  .label__content {
    position: absolute; inset: 0;
    display: flex; flex-direction: column; align-items: center;
  }
  .label__title {
    font-family: "Abril Fatface", serif;
    color: var(--copper);
    font-weight: 400;
    line-height: 1;
  }
  .label__title--mirabelle { font-size: 86px; margin-top: 118px; letter-spacing: -1px; }
  .label__subtitle {
    font-family: "Abril Fatface", serif;
    color: var(--copper);
    font-size: 48px; line-height: 1; margin-top: 8px;
  }
  .label__title--jojo {
    font-family: "Poiret One", sans-serif;
    font-size: 128px; margin-top: 54px; letter-spacing: 14px; font-weight: 400;
    -webkit-text-stroke: 2px var(--copper);
  }
  .label__subtitle--zwetschgen { font-size: 54px; margin-top: -4px; }
  .label__type {
    font-family: "Josefin Sans", sans-serif;
    font-size: 24px; font-weight: 400; letter-spacing: 1px;
    margin-top: 32px;
  }
  .label__producer {
    font-family: "Josefin Sans", sans-serif;
    font-size: 11.5px; margin-top: 30px;
  }
  .label__legal {
    display: flex; gap: 32px; align-items: baseline;
    font-family: "Josefin Sans", sans-serif;
    margin-top: 20px;
  }
  .label__volume, .label__abv { font-size: 17px; color: #8a6a3a; font-weight: 300; }
  .label__batch { font-size: 14px; width: 120px; text-align: left; }
</style>
</head>
<body>
<main class="sheet">
  <section class="label label--mirabelle">
    <div class="label__pattern" role="img" aria-label="Faint cream damask pattern background"></div>
    <div class="label__frame"></div>
    <div class="label__content">
      <h1 class="label__title label__title--mirabelle">Mirabelle</h1>
      <p class="label__subtitle">de Nancy</p>
      <p class="label__type">BRAND</p>
      <p class="label__producer">Hausbrennerei Tobias Wendelbrunn, Lindenweg 5, 68417 Vogtsburg</p>
      <div class="label__legal">
        <span class="label__volume">0,70 L</span>
        <span class="label__batch">Batch number:</span>
        <span class="label__abv">Alc. 42% vol.</span>
      </div>
    </div>
  </section>

  <section class="label label--jojo">
    <div class="label__pattern" role="img" aria-label="Faint cream damask pattern background"></div>
    <div class="label__frame"></div>
    <div class="label__content">
      <h1 class="label__title label__title--jojo">Jojo</h1>
      <p class="label__subtitle label__subtitle--zwetschgen">Zwetschgen</p>
      <p class="label__type">BRAND</p>
      <p class="label__producer">Hausbrennerei Tobias Wendelbrunn, Lindenweg 5, 68417 Vogtsburg</p>
      <div class="label__legal">
        <span class="label__volume">0,70 L</span>
        <span class="label__batch">Batch number:</span>
        <span class="label__abv">Alc. 42% vol.</span>
      </div>
    </div>
  </section>
</main>
</body>
</html>
```